Trivia Game

I need a website designed for a Wordpress site. The site will be a contest site that will allow players to compete in trivia contests for money, including crypto currencies.

Target Market(s)

people who want to play trivia games for cash

Industry/Entity Type

Games

Number of Pages Required

1 page

Colors

Designer to choose colors to be used in the design.

Requirements
Must have
• A place for a video. A call to action - Signup.
• Black and gold like a casino.
• Very classy
Nice to have
• attached are some examples of the style I want. Very sparkly, clean classy, like a casino.

```html
<!DOCTYPE html>
<html lang="en">
<head>
<meta charset="utf-8">
<title>Aurelo — Online Trivia Game</title>
<link href="https://fonts.googleapis.com/css2?family=Oswald:wght@400;500;600&family=Open+Sans:wght@400;600&display=swap" rel="stylesheet">
<style>
:root{
  --gold:#f5c200;
  --gold-deep:#e2a600;
  --gold-light:#ffd84a;
  --ink:#1f1f1f;
  --ink-2:#262626;
  --footer:#1b1b1b;
  --white:#ffffff;
  --muted:#bdbdbd;
  --line:#3a3a3a;
  --purple:#3b2a6b;
}
*{box-sizing:border-box;margin:0;padding:0}
html,body{width:1200px;height:2748px;overflow:hidden}
body{position:relative;background:var(--ink);font-family:"Open Sans",Arial,sans-serif;color:var(--white)}
.abs{position:absolute}
.head{font-family:"Oswald",Arial Narrow,sans-serif;text-transform:uppercase}

/* hero */
.hero{left:0;top:0;width:1200px;height:595px;background:radial-gradient(ellipse at 50% 40%,var(--gold-light),var(--gold) 45%,var(--gold-deep))}
.hero-art{left:290px;top:120px;width:910px;height:475px;background:linear-gradient(120deg,rgba(92,62,140,.35),rgba(255,216,74,.15) 50%,rgba(170,120,0,.45));border-radius:6px 0 0 0}
.logo{left:97px;top:30px;font-family:"Oswald",sans-serif;font-weight:600;font-size:44px;color:var(--white);letter-spacing:1px}
.nav{left:437px;top:50px;display:flex;gap:28px;font-family:"Oswald",sans-serif;font-size:17px;color:var(--white);text-transform:uppercase}
.btn-signup{left:882px;top:46px;width:98px;height:34px;background:var(--ink);color:var(--white);font:500 15px "Oswald",sans-serif;display:flex;align-items:center;justify-content:center;text-transform:uppercase}
.btn-register{left:994px;top:46px;width:106px;height:34px;border:2px solid var(--white);color:var(--white);font:500 15px "Oswald",sans-serif;display:flex;align-items:center;justify-content:center;text-transform:uppercase}
.hero-title{left:112px;top:300px;font:500 72px/76px "Oswald",sans-serif;color:var(--white)}
.chev{top:280px}

/* how it works */
.how-title{left:0;width:1200px;top:676px;text-align:center;font-weight:500;font-size:40px}
.step{top:776px;width:200px;height:200px;border-radius:50%;background:var(--gold);border:5px solid #8a8a8a;display:flex;flex-direction:column;align-items:center;justify-content:center;text-align:center}
.step-label{font:400 20px/25px "Oswald",sans-serif;color:var(--white);margin-top:10px}
.step-label b{font-weight:500;font-size:22px;text-transform:uppercase}

/* video */
.video{left:178px;top:1044px;width:844px;height:378px;border:4px solid var(--white);background:linear-gradient(180deg,#4b2c7e,#2d1b57 60%,#1b1438)}
.play{left:388px;top:165px;width:60px;height:40px;background:var(--gold);border-radius:4px}
.progress{left:100px;top:332px;width:620px;height:8px;background:#555}
.progress span{display:block;width:55%;height:100%;background:var(--gold)}

/* topics */
.topics-title{left:0;width:1200px;top:1470px;text-align:center;font-weight:500;font-size:40px;color:var(--white)}
.grid{left:99px;top:1561px;display:grid;grid-template-columns:repeat(4,238px);column-gap:16px;row-gap:25px}
.card{width:238px;height:242px;background:var(--white)}
.card-art{height:190px}
.card-label{height:52px;display:flex;align-items:center;justify-content:center;font:400 17px "Oswald",sans-serif;color:#222;text-transform:uppercase}

/* newsletter */
.news-icon{left:203px;top:2272px;width:62px;height:62px;border-radius:50%;background:var(--gold)}
.news-title{left:280px;top:2262px;font:500 34px "Oswald",sans-serif;color:#222}
.news-sub{left:281px;top:2306px;font:400 15px "Oswald",sans-serif;color:#333}
.news-input{left:578px;top:2278px;width:310px;height:42px;background:var(--white);border:1px solid #ddd;font-size:12px;color:#888;display:flex;align-items:center;padding-left:18px}
.news-btn{left:888px;top:2278px;width:126px;height:42px;background:var(--gold);color:var(--white);font:500 15px "Oswald",sans-serif;display:flex;align-items:center;justify-content:center;text-transform:uppercase}

/* footer */
.footer{left:0;top:2376px;width:1200px;height:372px;background:var(--footer)}
.f-title{top:2430px;font:500 22px "Oswald",sans-serif;text-transform:uppercase}
.links{left:99px;top:2480px;list-style:none;font-size:12px;line-height:25.5px}
.links li::before{content:"›";margin-right:14px;color:var(--white)}
.contact{left:317px;top:2482px;font-size:12px;line-height:19px}
.contact-row{display:flex;gap:14px;margin-bottom:12px}
.signup-text{left:635px;top:2476px;width:468px;font-size:11.5px;line-height:19px;color:#ddd}
.field{height:42px;border:1px solid #8a8a8a;font-size:11px;color:#ddd;display:flex;align-items:center;padding-left:14px}
.submit{left:877px;top:2577px;width:225px;height:42px;background:var(--gold);color:#111;font:500 16px "Oswald",sans-serif;display:flex;align-items:center;justify-content:center;text-transform:uppercase}
.rule{left:0;top:2680px;width:1200px;height:1px;background:var(--line)}
.copy{left:99px;top:2703px;font-size:13px}
.social{left:994px;top:2701px;display:flex;gap:6px}
.social span{width:24px;height:24px;border:1px solid #bbb;border-radius:50%}
</style>
</head>
<body>

<!-- hero -->
<section class="abs hero"></section>
<div class="abs hero-art" role="img" aria-label="Illustration of a cheering man at a desk holding a money bag beside a computer, with confetti and golden dice"></div>
<div class="abs logo">Aurelo</div>
<nav class="abs nav"><span>About</span><span>Trivia Game</span><span>Support</span><span>News</span><span>Contact Us</span></nav>
<a class="abs btn-signup">Sign Up</a>
<a class="abs btn-register">Register</a>
<h1 class="abs hero-title head">Online<br>Trivia<br>Game</h1>
<svg class="abs chev" style="left:48px" width="30" height="60" viewBox="0 0 30 60"><path d="M26 2 4 30l22 28" fill="none" stroke="#fff" stroke-opacity=".6" stroke-width="2"/></svg>
<svg class="abs chev" style="left:1122px" width="30" height="60" viewBox="0 0 30 60"><path d="M4 2l22 28L4 58" fill="none" stroke="#fff" stroke-opacity=".6" stroke-width="2"/></svg>

<!-- background split between dark and gold -->
<svg class="abs" style="left:0;top:595px" width="1200" height="1600" viewBox="0 0 1200 1600">
  <rect y="500" width="1200" height="1100" fill="var(--gold)"/>
  <polygon points="0,0 1200,0 1200,530 600,580 0,530" fill="var(--ink)"/>
</svg>
<svg class="abs" style="left:0;top:2180px" width="1200" height="200" viewBox="0 0 1200 200">
  <polygon points="0,60 600,10 1200,60 1200,200 0,200" fill="#f3f3f3"/>
</svg>

<!-- how it works -->
<h2 class="abs how-title head">How it works</h2>
<div class="abs step" style="left:175px">
  <svg width="46" height="46" viewBox="0 0 46 46"><circle cx="32" cy="14" r="9" fill="none" stroke="#fff" stroke-width="4"/><path d="M25 21 6 40m5-5 5 5m-10-0 4 4" stroke="#fff" stroke-width="4" fill="none"/></svg>
  <div class="step-label">Contact US &amp; Open<br><b>A Free Account</b></div>
  <svg width="14" height="14" viewBox="0 0 14 14"><path d="M2 2l5 5 5-5M2 7l5 5 5-5" fill="none" stroke="#fff" stroke-width="1.6"/></svg>
</div>
<div class="abs step" style="left:492px">
  <svg width="46" height="46" viewBox="0 0 46 46"><rect x="6" y="14" width="24" height="24" rx="4" fill="#fff"/><rect x="20" y="4" width="20" height="20" rx="4" fill="#fff" stroke="var(--gold)" stroke-width="2"/><circle cx="12" cy="20" r="2" fill="var(--gold)"/><circle cx="24" cy="32" r="2" fill="var(--gold)"/><circle cx="30" cy="14" r="2" fill="var(--gold)"/></svg>
  <div class="step-label">Choose Your Trivia<br>Game</div>
  <svg width="14" height="14" viewBox="0 0 14 14"><path d="M2 2l5 5 5-5M2 7l5 5 5-5" fill="none" stroke="#fff" stroke-width="1.6"/></svg>
</div>
<div class="abs step" style="left:818px">
  <svg width="46" height="46" viewBox="0 0 46 46"><path d="M16 6h14l-4 8c9 4 12 12 12 18 0 6-6 10-15 10S8 38 8 32c0-6 3-14 12-18z" fill="#fff"/><text x="23" y="36" text-anchor="middle" font-family="Oswald" font-size="16" font-weight="600" fill="var(--gold)">$</text></svg>
  <div class="step-label">Trivia Contests<br>For Money</div>
  <svg width="14" height="14" viewBox="0 0 14 14"><path d="M2 2l5 5 5-5M2 7l5 5 5-5" fill="none" stroke="#fff" stroke-width="1.6"/></svg>
</div>
<svg class="abs" style="left:400px;top:850px" width="72" height="20" viewBox="0 0 72 20"><path d="M2 16Q36 0 64 8" fill="none" stroke="var(--gold)" stroke-width="2" stroke-dasharray="5 4"/><path d="M60 3l7 5-8 3" fill="none" stroke="var(--gold)" stroke-width="2"/></svg>
<svg class="abs" style="left:725px;top:910px" width="72" height="20" viewBox="0 0 72 20"><path d="M2 6Q36 20 64 10" fill="none" stroke="var(--gold)" stroke-width="2" stroke-dasharray="5 4"/><path d="M59 6l8 4-7 5" fill="none" stroke="var(--gold)" stroke-width="2"/></svg>

<!-- video -->
<div class="abs video" role="img" aria-label="Video of a televised trivia game show with contestants at podiums and a million dollar prize sign">
  <div class="abs play"><svg width="60" height="40" viewBox="0 0 60 40"><path d="M25 12v16l13-8z" fill="#222"/></svg></div>
  <div class="abs progress"><span></span></div>
</div>

<!-- topics -->
<h2 class="abs topics-title head">Popular Quiz Topics</h2>
<div class="abs grid">
  <div class="card"><div class="card-art" role="img" aria-label="Pop music artwork with a music note icon" style="background:linear-gradient(135deg,#6b4a2e,#3a2a20)"></div><div class="card-label">Pop Music</div></div>
  <div class="card"><div class="card-art" role="img" aria-label="Movie theatre scene with a clapperboard icon" style="background:linear-gradient(135deg,#4a3a4e,#2e2a30)"></div><div class="card-label">Movie</div></div>
  <div class="card"><div class="card-art" role="img" aria-label="World map with a globe icon" style="background:linear-gradient(135deg,#7a6e58,#5b5244)"></div><div class="card-label">Geography</div></div>
  <div class="card"><div class="card-art" role="img" aria-label="Science doodles with a lab flask icon" style="background:linear-gradient(135deg,#7d7570,#5d5753)"></div><div class="card-label">Science</div></div>
  <div class="card"><div class="card-art" role="img" aria-label="Office computers with a code screen icon" style="background:linear-gradient(135deg,#4a4540,#2f2c2a)"></div><div class="card-label">Computer</div></div>
  <div class="card"><div class="card-art" role="img" aria-label="Concert hall with a piano keys icon" style="background:linear-gradient(135deg,#6a4030,#3b2820)"></div><div class="card-label">Classical Music</div></div>
  <div class="card"><div class="card-art" role="img" aria-label="Historic map with a history clock icon" style="background:linear-gradient(135deg,#6a6660,#4a4744)"></div><div class="card-label">History</div></div>
  <div class="card"><div class="card-art" role="img" aria-label="Desk with glasses and notebook and a light bulb icon" style="background:linear-gradient(135deg,#4a4038,#2d2824)"></div><div class="card-label">Miscellaneous</div></div>
</div>

<!-- newsletter -->
<div class="abs news-icon"><svg width="62" height="62" viewBox="0 0 62 62"><rect x="19" y="22" width="24" height="17" rx="2" fill="none" stroke="#fff" stroke-width="2.4"/><path d="M19 24l12 9 12-9" fill="none" stroke="#fff" stroke-width="2.4"/></svg></div>
<div class="abs news-title">Join our Newsletter.</div>
<div class="abs news-sub">Stay up to date with the latest news.</div>
<div class="abs news-input">Enter Your Email</div>
<div class="abs news-btn">Subscribe</div>

<!-- footer -->
<footer class="abs footer"></footer>
<h3 class="abs f-title" style="left:99px">Quick Links</h3>
<ul class="abs links"><li>Home</li><li>About Us</li><li>Play now</li><li>Trivia game</li><li>Promotions</li><li>Explore</li></ul>
<h3 class="abs f-title" style="left:317px">Contact Us</h3>
<div class="abs contact">
  <div class="contact-row"><svg width="12" height="16" viewBox="0 0 12 16"><path d="M6 1a5 5 0 0 0-5 5c0 4 5 9 5 9s5-5 5-9a5 5 0 0 0-5-5z" fill="#fff"/><circle cx="6" cy="6" r="2" fill="var(--footer)"/></svg><div>Aurelo<br>4410 KM&nbsp; Veldhaven The Netherlands</div></div>
  <div class="contact-row" style="font-size:13px"><svg width="12" height="14" viewBox="0 0 12 14"><path d="M2 1l3 0 1 3-2 1.5a8 8 0 0 0 3 3L8.5 7l3 1v3c0 1-1 2-2 2C5 13 0 8 0 3c0-1 1-2 2-2z" fill="#fff"/></svg><div>Phone : 1 555 204 7719</div></div>
  <div class="contact-row" style="font-size:13px"><svg width="12" height="14" viewBox="0 0 12 14"><rect y="3" width="12" height="8" fill="#fff"/><path d="M0 3l6 4 6-4" fill="none" stroke="var(--footer)"/></svg><div>Email : info@aurelo-play.com</div></div>
</div>
<h3 class="abs f-title" style="left:635px">Quick Signup</h3>
<p class="abs signup-text">Lorem ipsum dolor sit amet, consectetur adipiscing elit, sed do eiusmod tempor incididunt ut labore et dolore magna aliqua. Ut enim ad minim veniam,</p>
<div class="abs field" style="left:635px;top:2526px;width:226px">Name</div>
<div class="abs field" style="left:877px;top:2526px;width:225px">E - Mail</div>
<div class="abs field" style="left:635px;top:2577px;width:226px">Phone No</div>
<div class="abs submit">Submit Now!</div>
<div class="abs rule"></div>
<div class="abs copy">© 2018 Aurelo. All Rights Reserved.</div>
<div class="abs social"><span></span><span></span><span></span><span></span></div>

</body>
</html>
```